Fahrzeugbeschriftung für Handwerksunternehmen im Elektro-Bereich
Zielgruppe
Die Firma Kalbe & Wunsch Elektrotechnik GmbH & Co. KG ist ein Handwerksunternehmen und führt sämtliche Dienstleistungen im Elektrohandwerk durch wie z.B. Kundendienst , Netzwerktechnik , Gebäudetechnik ,
Unsere Zielgruppe sind Gewerbe sowie Privatkunden.
Aufgabenstellung
Das Design soll hochwertig , durchdacht und modern wirken.
Unser Logo soll mit eingebunden werden sowie unsere Internetseite www.kalbe-wunsch.de.
Es müssen zwei Ausführungen des Designs erstellt werden :
Fahrzeuge : Varnel Kobano L2H1 2013 sowie Duvalle Fargon 2013 L1H1
Beide Fahrzeuge sind weiß, keine Fenster im Ladebereich.

```html
<!DOCTYPE html>
<html lang="de">
<head>
<meta charset="utf-8">
<title>Kalbe &amp; Wunsch Elektrotechnik – Fahrzeugbeschriftung</title>
<link rel="stylesheet" href="https://fonts.googleapis.com/css2?family=Open+Sans:wght@400;600;700&display=swap">
<style>
  :root {
    --stage: #e6e6e6;
    --panel: #f7f7f7;
    --panel-edge: #d4d4d4;
    --brand-blue: #1b7fc4;
    --brand-deep: #0b72bf;
    --brand-light: #1e8fcc;
    --teal: #11979b;
    --navy: #2f4f7f;
    --sky: #2aa0dc;
    --ink: #4a4a4a;
    --white: #ffffff;
  }
  html, body { margin: 0; padding: 0; overflow: hidden; }
  body {
    width: 786px; height: 1200px;
    background: var(--stage);
    font-family: "Open Sans", Arial, sans-serif;
    color: var(--ink);
  }
  .canvas { position: relative; width: 786px; height: 1200px; }
  .section { position: absolute; left: 0; width: 786px; }
  .side-view { top: 0; height: 449px; background: var(--stage); }
  .brand-block {
    top: 449px; height: 306px;
    background: linear-gradient(180deg, var(--brand-deep) 0%, var(--brand-light) 100%);
  }
  .rear-view { top: 755px; height: 445px; background: var(--stage); }
  svg { display: block; font-family: "Open Sans", Arial, sans-serif; }
</style>
</head>
<body>
<main class="canvas">

  <section class="section side-view" aria-label="Seitenansicht der Beschriftung">
    <svg width="786" height="449" viewBox="0 0 786 449">
      <defs>
        <linearGradient id="icon-field" x1="0" y1="0" x2="1" y2="0">
          <stop offset="0" stop-color="#cfe6f4"/>
          <stop offset="0.5" stop-color="#bcdcf0"/>
          <stop offset="1" stop-color="#c6e6e6"/>
        </linearGradient>
      </defs>
      <rect class="side-panel" x="100" y="165" width="590" height="205" rx="14" fill="var(--panel)" stroke="var(--panel-edge)"/>
      <path d="M100 312 L350 312 L290 328 L100 330 Z" fill="var(--brand-blue)"/>
      <path d="M250 348 L350 326 L690 318 L690 344 L240 348 Z" fill="var(--teal)"/>
      <rect x="100" y="350" width="590" height="20" fill="#3a3a3a"/>

      <g class="icon-network" role="img" aria-label="Illustration: vernetzte Leistungssymbole rund um das Firmenzeichen">
        <rect x="398" y="188" width="212" height="66" rx="10" fill="url(#icon-field)"/>
      </g>

      <g class="wordmark" fill="var(--brand-blue)" font-weight="700">
        <text x="509" y="281" text-anchor="middle" font-size="20" letter-spacing="1">KALBE &amp; WUNSCH</text>
        <text x="509" y="298" text-anchor="middle" font-size="10" letter-spacing="2.5">ELEKTROTECHNIK</text>
      </g>
      <g stroke="var(--ink)" stroke-width="0.7">
        <line x1="412" y1="294" x2="450" y2="294"/>
        <line x1="568" y1="294" x2="608" y2="294"/>
      </g>

      <circle cx="251" cy="301" r="6" fill="var(--ink)"/>
      <path d="M248.5 298 q1 4 5 5.5 l1-1.5 -1.5-1 -1 1 q-1.5-.8-2-2 l1-1 -1-1.5 z" fill="var(--panel)"/>
      <text x="262" y="306" font-size="12" fill="var(--ink)">040-61837204</text>
      <text x="443" y="338" text-anchor="middle" font-size="10" font-weight="600" fill="var(--white)">www.kalbe-wunsch.de</text>
    </svg>
  </section>

  <section class="section brand-block" aria-label="Markenzeichen">
    <svg width="786" height="306" viewBox="0 0 786 306">
      <circle class="mark-spot" cx="400" cy="134" r="38" fill="none" stroke="var(--white)" stroke-width="3"/>
      <g class="wordmark" fill="var(--white)" font-weight="700">
        <text x="409" y="205" text-anchor="middle" font-size="25" letter-spacing="1">KALBE &amp; WUNSCH</text>
        <text x="409" y="225" text-anchor="middle" font-size="11" letter-spacing="3.5">ELEKTROTECHNIK</text>
      </g>
      <g stroke="var(--white)" stroke-width="1">
        <line x1="294" y1="221" x2="336" y2="221"/>
        <line x1="482" y1="221" x2="524" y2="221"/>
      </g>
    </svg>
  </section>

  <section class="section rear-view" aria-label="Heckansicht der Beschriftung">
    <svg width="786" height="445" viewBox="0 0 786 445">
      <rect class="rear-panel" x="252" y="40" width="306" height="290" rx="12" fill="var(--panel)" stroke="var(--panel-edge)"/>
      <line x1="405" y1="40" x2="405" y2="330" stroke="var(--panel-edge)" stroke-width="1.5"/>

      <circle class="mark-spot" cx="403" cy="97" r="28" fill="none" stroke="var(--brand-blue)" stroke-width="2.5"/>
      <g class="wordmark" fill="var(--brand-blue)" font-weight="700">
        <text x="403" y="151" text-anchor="middle" font-size="19" letter-spacing="1">KALBE &amp; WUNSCH</text>
        <text x="403" y="169" text-anchor="middle" font-size="9.5" letter-spacing="2.5">ELEKTROTECHNIK</text>
      </g>
      <g stroke="var(--ink)" stroke-width="0.7">
        <line x1="298" y1="165" x2="338" y2="165"/>
        <line x1="468" y1="165" x2="508" y2="165"/>
      </g>

      <g class="services" font-size="8.5" fill="var(--ink)" letter-spacing="0.6">
        <circle cx="440" cy="193" r="6" fill="var(--sky)"/>
        <text x="451" y="196">GEBÄUDETECHNIK</text>
        <circle cx="440" cy="210" r="6" fill="var(--navy)"/>
        <text x="451" y="213">NETZWERKTECHNIK</text>
        <circle cx="440" cy="227" r="6" fill="var(--teal)"/>
        <text x="451" y="230">KUNDENDIENST</text>
      </g>

      <path d="M252 245 L350 245 L440 263 L252 263 Z" fill="var(--teal)"/>
      <path d="M405 245 L558 245 L558 263 L485 263 Z" fill="var(--brand-blue)"/>
      <text x="272" y="259" font-size="9" font-weight="600" fill="var(--white)">www.kalbe-wunsch.de</text>

      <circle cx="440" cy="298" r="6" fill="var(--ink)"/>
      <path d="M437.5 295 q1 4 5 5.5 l1-1.5 -1.5-1 -1 1 q-1.5-.8-2-2 l1-1 -1-1.5 z" fill="var(--panel)"/>
      <text x="451" y="302" font-size="11.5" fill="var(--ink)">040-61837204</text>
    </svg>
  </section>

</main>
</body>
</html>
```